Self Defence Seminar Flyer

Need a flyer that will sell a seminar that will teach self defence techniques to customers. Needs to have a good image that will remind people about the dangerous world. The seminar is for men and women.

Needs to look professional.

I have attached the previous flyer we used. needs same information except without the same date and time for seminar.

Target Market(s)

Male and Females interested in learning how to defend themselves or family

Industry/Entity Type

Defence

Requirements
Must have
• A Image that reminds people of a dangerous situation

```html
<!DOCTYPE html>
<html lang="en">
<head>
<meta charset="utf-8">
<title>Self Defence Seminar</title>
<link href="https://fonts.googleapis.com/css2?family=Oswald:wght@500;700&family=Roboto+Condensed:wght@400;700&family=Arimo:wght@400&display=swap" rel="stylesheet">
<style>
  :root {
    --orange: #f6a31b;
    --red: #e3232b;
    --ink: #1a1a1a;
    --grey-top: #c9c9c9;
    --paper: #ffffff;
    --bar: #1c1c1c;
    --social: #1d4f8f;
  }
  * { box-sizing: border-box; margin: 0; padding: 0; }
  html, body { width: 1200px; height: 900px; overflow: hidden; background: var(--paper); }
  .flyer {
    position: absolute; left: 278px; top: 3px; width: 632px; height: 894px;
    border: 1px solid #555;
    background: linear-gradient(180deg, var(--grey-top) 0%, #efefef 40%, var(--paper) 60%);
    overflow: hidden;
    font-family: "Arimo", Arial, sans-serif; color: var(--ink);
  }
  .hero-art { position: absolute; left: 0; top: 0; width: 632px; height: 620px; }
  .title { font-family: "Oswald", sans-serif; font-weight: 700; line-height: 1; }
  .title span { position: absolute; white-space: nowrap; transform-origin: left top; }
  .title-accent { left: 18px; top: 20px; font-size: 90px; color: var(--orange); -webkit-text-stroke: 2.5px var(--ink); transform: scaleX(0.61); }
  .title-main { left: 334px; top: 8px; font-size: 100px; color: var(--ink); transform: scaleX(0.74); }
  .point { position: absolute; right: 18px; font-size: 14.5px; line-height: 19px; text-align: right; white-space: nowrap; }
  .point-1 { top: 125px; }
  .point-2 { top: 249px; }
  .point-3 { top: 355px; }
  .point-4 { top: 441px; }
  .point-5 { top: 527px; }
  .cost {
    position: absolute; left: 24px; top: 575px; width: 126px; height: 126px; border-radius: 50%;
    background: var(--red); border: 4px solid var(--paper); box-shadow: 0 0 0 1px #ccc;
    color: var(--paper); text-align: center; font-family: "Roboto Condensed", sans-serif; font-weight: 700;
  }
  .cost-label { display: block; font-size: 26px; margin-top: 16px; }
  .cost-amount { display: block; font-size: 46px; line-height: 1; }
  .cost-amount sup { font-size: 22px; vertical-align: 20px; }
  .cost-amount .dollar { font-size: 24px; vertical-align: 18px; }
  .location { position: absolute; left: 160px; top: 600px; width: 460px; text-align: center; font-family: "Roboto Condensed", sans-serif; }
  .location-label { font-size: 27px; font-weight: 700; }
  .location-name { font-size: 33px; font-weight: 700; color: var(--red); margin-top: 4px; }
  .location-address { font-size: 23px; margin-top: 2px; }
  .social { position: absolute; left: 22px; top: 722px; font-family: "Roboto Condensed", sans-serif; font-size: 25px; color: var(--social); }
  .social-row { display: flex; align-items: center; gap: 6px; height: 32px; }
  .social-row i { width: 26px; height: 26px; background: var(--social); display: inline-block; }
  .signup {
    position: absolute; left: 197px; top: 718px; width: 435px; height: 51px;
    background: var(--bar); border-radius: 10px 0 0 10px; color: var(--paper); text-align: center;
    font-family: "Roboto Condensed", sans-serif; font-weight: 700; padding-top: 5px;
  }
  .signup-line { font-size: 17px; }
  .signup-url { font-size: 20px; }
  .brand { position: absolute; top: 790px; height: 92px; display: flex; align-items: center; justify-content: center; font-family: "Oswald", sans-serif; font-weight: 700; text-align: center; }
  .brand-team { left: 18px; width: 224px; font-size: 28px; color: var(--orange); }
  .brand-academy { left: 298px; width: 137px; font-size: 18px; color: #888; }
  .badge-partner { position: absolute; left: 509px; top: 782px; width: 100px; height: 100px; background: #3a3a3a; }
</style>
</head>
<body>
  <div class="flyer">
    <svg class="hero-art" viewBox="0 0 632 620" xmlns="http://www.w3.org/2000/svg">
      <defs>
        <linearGradient id="photoTone" x1="0" y1="0" x2="1" y2="1">
          <stop offset="0" stop-color="#8a98aa"/>
          <stop offset="0.45" stop-color="#5c6a80"/>
          <stop offset="0.75" stop-color="#4a2e6a"/>
          <stop offset="1" stop-color="#9fb4c8"/>
        </linearGradient>
      </defs>
      <circle cx="132" cy="342" r="257" fill="none" stroke="var(--orange)" stroke-width="10"/>
      <circle cx="122" cy="337" r="250" fill="url(#photoTone)" role="img" aria-label="Photo: young woman in a knit hat, scarf and purple coat glancing back in a cold walkway as a dark hooded figure approaches behind her"/>
    </svg>

    <h1 class="title"><span class="title-accent">SELF DEFENCE</span><span class="title-main">SEMINAR</span></h1>

    <p class="point point-1">• Being a victim is a topic that people<br>would like to avoid. Unfortunately, we<br>live in an increasingly dangerous<br>society for men and women alike.<br>Learning to defend yourself is an<br>important life skill.</p>
    <p class="point point-2">• Spend 2 Hours with us learning<br>some simple and effective<br>Self Defence tactics that one-<br>day may be needed to defend<br>yourself or loved ones.</p>
    <p class="point point-3">• Our aim is to teach you<br>effective and efficient techniques<br>and tactics to be able to defend<br>yourself in a range of situations.</p>
    <p class="point point-4">• Learn the same techniques<br>and tactics that we have taught<br>to individuals in Law enforcement,<br>Security, and Military.</p>
    <p class="point point-5">• We incorporate weapon defence, use of<br>surroundings and psychological techniques<br>in our classes.</p>

    <div class="cost">
      <span class="cost-label">Cost:</span>
      <span class="cost-amount"><span class="dollar">$</span>60<sup>00</sup></span>
    </div>

    <div class="location">
      <div class="location-label">Location:</div>
      <div class="location-name">Ironside Combat Gym</div>
      <div class="location-address">(214 Wattle Rd. Riverbend NSW)</div>
    </div>

    <div class="social">
      <div class="social-row"><i></i>/IRONSIDEAU</div>
      <div class="social-row"><i></i>#IRONSIDEAU</div>
    </div>

    <div class="signup">
      <div class="signup-line">Sign up today by contacting us through our website</div>
      <div class="signup-url">www.ironsidecombat.com</div>
    </div>

    <div class="brand brand-team">TEAM IRONSIDE</div>
    <div class="brand brand-academy">Ironside Academy</div>
    <div class="badge-partner" role="img" aria-label="Partner badge"></div>
  </div>
</body>
</html>
```